Business Card Design

We need a business card for a new business based in Sydney, Australia. It is a home based baking business, the key products are cookies and muffins and slices including gluten free baked goods. With the emphasis on home made baking. The target market is cafes, coffee shops and vans, restaurants. Products may be provided in display jars or individually wrapped. The final design should be in the colours pink, purple.

Business

Tindle's Bakery Pty Ltd, Marisa Pellow, marisa@tindlesbakery.com.au
0451 276 308, www.tindlesbakery.com.au, ACN 512 648 397,

```html
<!DOCTYPE html>
<html lang="en">
<head>
<meta charset="utf-8">
<title>Tindle's Bakery – Business Card</title>
<link rel="stylesheet" href="https://fonts.googleapis.com/css2?family=Fira+Sans+Condensed:wght@500;700&family=Lato:wght@400&display=swap">
<style>
  :root {
    --page-bg: #ece8e3;
    --card-bg: #ffffff;
    --pink: #f5148c;
    --pink-soft: #ff7cc4;
    --purple: #b424d6;
    --contact: #c23ccf;
    --cookie-light: #f3e9da;
    --cookie-mid: #e6d6bf;
    --basket-warm: #e4d2ba;
    --basket-deep: #d6bfa3;
    --white: #ffffff;
  }
  * { margin: 0; padding: 0; box-sizing: border-box; }
  html, body {
    width: 1200px;
    height: 800px;
    overflow: hidden;
    background: var(--page-bg);
  }
  .canvas {
    position: relative;
    width: 1200px;
    height: 800px;
  }
  .card {
    position: absolute;
    left: 75px;
    top: 86px;
    width: 640px;
    height: 383px;
    transform: scale(1.64);
    transform-origin: top left;
    background: var(--card-bg);
    border-radius: 9px;
    overflow: hidden;
    box-shadow: 0 2px 6px rgba(0,0,0,0.18);
  }
  .photo-cookie {
    position: absolute;
    left: 0; top: 0;
    width: 400px; height: 330px;
    background: linear-gradient(90deg, var(--cookie-light) 0%, var(--cookie-mid) 55%, rgba(255,255,255,0) 100%);
  }
  .photo-basket {
    position: absolute;
    left: 360px; top: 0;
    width: 280px; height: 330px;
    background: linear-gradient(90deg, rgba(255,255,255,0) 0%, var(--basket-warm) 35%, var(--basket-deep) 100%);
  }
  .brand {
    position: absolute;
    left: 26px;
    top: 18px;
    font-family: "Fira Sans Condensed", sans-serif;
    font-weight: 700;
    color: var(--pink);
    line-height: 0.92;
  }
  .brand-name { font-size: 104px; letter-spacing: 3px; }
  .brand-tail { font-size: 50px; letter-spacing: 0.5px; }
  .contact-list {
    position: absolute;
    left: 28px;
    top: 240px;
    list-style: none;
    font-family: "Lato", sans-serif;
    font-size: 13.5px;
    color: var(--contact);
  }
  .contact-item {
    display: flex;
    align-items: center;
    height: 23px;
  }
  .contact-icon {
    width: 14px; height: 14px;
    margin-right: 9px;
    flex: none;
  }
  .footer-band {
    position: absolute;
    left: 0; bottom: 0;
    width: 640px; height: 62px;
  }
  .holder-name {
    position: absolute;
    right: 13px;
    bottom: 9px;
    font-family: "Fira Sans Condensed", sans-serif;
    font-weight: 700;
    font-size: 34px;
    line-height: 1;
    letter-spacing: 0.5px;
    color: var(--white);
  }
  .holder-surname { color: var(--pink-soft); }
</style>
</head>
<body>
<main class="canvas">
  <article class="card">
    <div class="photo-cookie" role="img" aria-label="Faded close-up photograph of a chocolate chip cookie"></div>
    <div class="photo-basket" role="img" aria-label="Photograph of a gift basket of wrapped muffins, plates of cookies and chocolate slices"></div>

    <h1 class="brand">
      <span class="brand-name">Tindle's</span><br>
      <span class="brand-tail">Bakery Pty Ltd,</span>
    </h1>

    <ul class="contact-list">
      <li class="contact-item">
        <svg class="contact-icon" viewBox="0 0 14 14"><path d="M7 1a4.2 4.2 0 0 0-4.2 4.2C2.8 8.4 7 13 7 13s4.2-4.6 4.2-7.8A4.2 4.2 0 0 0 7 1zm0 5.9a1.7 1.7 0 1 1 0-3.4 1.7 1.7 0 0 1 0 3.4z" fill="currentColor"/></svg>
        ACN 512 648 397,
      </li>
      <li class="contact-item">
        <svg class="contact-icon" viewBox="0 0 14 14"><rect x="3.5" y="0.8" width="7" height="12.4" rx="1.2" fill="none" stroke="currentColor" stroke-width="1.2"/><line x1="5.8" y1="11" x2="8.2" y2="11" stroke="currentColor" stroke-width="1"/></svg>
        0451 276 308
      </li>
      <li class="contact-item">
        <svg class="contact-icon" viewBox="0 0 14 14"><rect x="1" y="3" width="12" height="8.5" rx="1" fill="currentColor"/><path d="M1.5 3.8 7 7.8l5.5-4" fill="none" stroke="#fff" stroke-width="1"/></svg>
        marisa@tindlesbakery.com.au
      </li>
      <li class="contact-item">
        <svg class="contact-icon" viewBox="0 0 14 14"><rect x="1" y="1.8" width="12" height="8.4" rx="0.8" fill="none" stroke="currentColor" stroke-width="1.2"/><rect x="5.5" y="10.2" width="3" height="1.8" fill="currentColor"/><rect x="3.8" y="12" width="6.4" height="1" fill="currentColor"/></svg>
        www.tindlesbakery.com.au
      </li>
    </ul>

    <svg class="footer-band" viewBox="0 0 640 62" aria-hidden="true">
      <defs>
        <linearGradient id="bandPurple" x1="0" y1="0" x2="1" y2="0">
          <stop offset="0" stop-color="#b424d6"/>
          <stop offset="1" stop-color="#c93ce0"/>
        </linearGradient>
      </defs>
      <rect x="0" y="0" width="640" height="62" fill="#ffffff" opacity="0"/>
      <polygon points="0,23 325,23 321,31 0,31" fill="#f5148c"/>
      <polygon points="0,40 640,40 640,62 0,62" fill="url(#bandPurple)"/>
      <polygon points="336,0 640,0 640,62 312,62" fill="url(#bandPurple)"/>
    </svg>
    <p class="holder-name">MARISA <span class="holder-surname">PELLOW</span></p>
  </article>
</main>
</body>
</html>
```